Label Design for American Pet Health Startup

We need your help in creating a line-up of labels for our upcoming products. The products will come in two different sizes/shapes. We have a logo (sourced form GraphiHive!) to start from and a pretty extensive brief (see attached.) The winning design will be bold, simple, and create a strongly branded look to the whole line while allowing consumers to easily sort through the different SKUs.

The logo and other existing design elements are in the attached powerpoint. I will also post some of the source files.

If you choose to compete for this project, please read the creative brief and the powerpoint very carefully before starting.

Thank you for your time and consideration.

Target Market(s)

Pet owners (dog owners, initially) who care deeply about their pets. Their pets are older and may not be thriving the way they once were. The owners want their pets to have the highest quality of life possible, for as long as is practical. They take their pets frequently to the vet and have great faith in veterinary medicine, but they also believe that dietary supplements may have a beneficial effect. They believe this to be possible because they take supplements themselves.

They are probably older--empty nesters or soon to be. They’ve owned their dog for five years or more, or have rescued an older dog from a shelter. Their dog is, in many ways, a full member of their family.

Industry/Entity Type

Pet Care

Font styles to use
Sans Serif

Requirements
Must have
• Please see the attached brief for this detail. I have cut and paste it into this form but it doesn't translate well. Reading the Word document will be easier and the links will work.
• Packaging Creative Considerations: The product packaging needs to . . .
• • Have a strong, branded line look.
• - The logo has already been developed, and I would like you to be guided in your design choices by its structure and color, but I am open to deviations from the existing work if it leads to a strong design
• • Use color or some other design elements to distinguish each SKU from the other
• • Be bold and simple. This product will typically be merchandised online, with very small images of the packaging. Simple and bold design elements will ensure that the products are both noticed and understood.
• - The product will likely be contained within white plastic or aluminum (silver) bottles with white caps/pumps. However, if you believe your design concepts would benefit from a particular color of bottle/container, please illustrate that, as that would be possible to execute.
• • Communicate that these products are for pets without using any clichés. This category is full of packaging with stock photos of dogs and cats. Please avoid this at all costs. Instead, please unleash your creativity to illustrate the products’ nature/purposes.
• A couple of packaging designs I would like you to draw inspiration from:
• o Vemo. This line is for human supplements/vitamins. Notice the strong line look, the simple and bold graphics, and the smart use of color and other design elements to differentiate the SKUs (while still holding it together as a single brand.)
• o Tundo. This line is for pets. Again, notice the strong line look, the smart use of color to differentiate the SKUs, and the simple and bold presentation that translates so well on the screen.
• o Corvalune. This design is not as good as the first two, but it does accomplish several of the brief’s objectives and the packaging is likely to be very similar to what your design will eventually be affixed to.
• Design Deliverables: A great submission will illustrate its strength by showing how the design translates across all the expected SKUs. To accomplish, this, I would recommend using the “functional maps” I’ve included in the attached Powerpoint document to:
• o First illustrate, in greater size and detail, one SKU each of the two families (one oil SKU and one supplement SKU)
• o Then illustrate how each of those designs extends across the rest of the family. That illustration can be less detailed. We just need to see how the colors and other design elements extend.
Should not have
• No stock images of cats or dogs; please avoid junking up the designs with too many elements

```html
<!DOCTYPE html>
<html lang="en">
<head>
<meta charset="utf-8">
<title>Pawmora Supplement Labels</title>
<link rel="stylesheet" href="https://fonts.googleapis.com/css2?family=Montserrat:wght@400;500;600;700&family=Didact+Gothic&display=swap">
<style>
  :root {
    --canvas: #f4f5f6;
    --label: #ffffff;
    --label-edge: #e3e5e8;
    --brand-teal: #1aa6b7;
    --joint-green: #8cc63f;
    --digest-pink: #e27d88;
    --body-grey: #6d6e71;
    --ink: #1d1d1f;
    --muted: #8a8b8e;
  }
  * { box-sizing: border-box; margin: 0; padding: 0; }
  html, body {
    width: 1200px;
    height: 1040px;
    overflow: hidden;
    background: var(--canvas);
  }
  .lineup {
    position: relative;
    width: 1200px;
    height: 1040px;
    display: flex;
    justify-content: center;
    align-items: center;
    gap: 112px;
  }
  .label {
    --sku: var(--joint-green);
    position: relative;
    width: 460px;
    height: 420px;
    background: var(--label);
    border: 1px solid var(--label-edge);
    border-radius: 6px;
    display: flex;
    flex-direction: column;
    align-items: center;
    padding-top: 44px;
    font-family: "Montserrat", sans-serif;
  }
  .label--digestion { --sku: var(--digest-pink); }
  .brand {
    display: flex;
    align-items: center;
    gap: 10px;
    height: 40px;
  }
  .brand__dot {
    width: 26px;
    height: 26px;
    border-radius: 50%;
    background: var(--brand-teal);
  }
  .brand__name {
    font-family: "Montserrat", sans-serif;
    font-weight: 400;
    font-size: 29px;
    color: var(--brand-teal);
    letter-spacing: 0.5px;
  }
  .product-name {
    margin-top: 12px;
    font-weight: 600;
    font-size: 50px;
    line-height: 1;
    color: var(--sku);
    letter-spacing: 0.5px;
  }
  .benefit {
    margin-top: 14px;
    font-weight: 500;
    font-size: 13.5px;
    line-height: 17px;
    color: var(--body-grey);
    text-align: center;
    letter-spacing: 0.3px;
  }
  .sku-emblem {
    margin-top: 14px;
    width: 50px;
    height: 50px;
    border-radius: 50%;
    background: var(--sku);
  }
  .format {
    margin-top: 14px;
    font-family: "Didact Gothic", sans-serif;
    font-size: 19px;
    color: var(--ink);
    letter-spacing: 0.3px;
  }
  .audience {
    margin-top: 2px;
    font-weight: 700;
    font-size: 20px;
    color: var(--sku);
    letter-spacing: 1px;
  }
  .count {
    margin-top: 8px;
    font-weight: 500;
    font-size: 13.5px;
    color: var(--ink);
    letter-spacing: 0.3px;
  }
  .net-weight {
    margin-top: 8px;
    font-weight: 400;
    font-size: 11px;
    color: var(--muted);
  }
  .badge {
    position: absolute;
    bottom: 46px;
    border: 1px solid var(--brand-teal);
    color: var(--brand-teal);
    font-family: "Didact Gothic", sans-serif;
    font-size: 12.5px;
    line-height: 14.5px;
    padding: 6px 8px;
  }
  .badge--origin {
    left: 30px;
    width: 53px;
    text-align: center;
  }
  .badge--free-from {
    right: 30px;
    width: 74px;
    text-align: left;
  }
</style>
</head>
<body>
<main class="lineup">

  <section class="label label--hip-joint">
    <div class="brand">
      <span class="brand__dot"></span>
      <span class="brand__name">Pawmora</span>
    </div>
    <h1 class="product-name">HIP &amp; JOINT</h1>
    <p class="benefit">Supports Healthy Joints with Glucosamine,<br>Chondroitin &amp; Willow Bark</p>
    <div class="sku-emblem" role="img" aria-label="Green circular emblem with a dog head illustration"></div>
    <p class="format">Soft &amp; Chewable Supplements</p>
    <p class="audience">FOR DOGS</p>
    <p class="count">90 Chews</p>
    <p class="net-weight">Net Wt 16 OZ / 453 g</p>
    <div class="badge badge--origin">Made<br>in<br>USA</div>
    <div class="badge badge--free-from">No Gluten<br>No Grain<br>No Soy</div>
  </section>

  <section class="label label--digestion">
    <div class="brand">
      <span class="brand__dot"></span>
      <span class="brand__name">Pawmora</span>
    </div>
    <h1 class="product-name">DIGESTION</h1>
    <p class="benefit">Supports Healthy Digestion<br>with Enzymes, Pre-Biotics &amp; Pro-Biotics</p>
    <div class="sku-emblem" role="img" aria-label="Pink circular emblem with a dog head illustration"></div>
    <p class="format">Soft &amp; Chewable Supplements</p>
    <p class="audience">FOR DOGS</p>
    <p class="count">90 Chews</p>
    <p class="net-weight">Net Wt 16 OZ / 453 g</p>
    <div class="badge badge--origin">Made<br>in<br>USA</div>
    <div class="badge badge--free-from">No Gluten<br>No Grain<br>No Soy</div>
  </section>

</main>
</body>
</html>
```